Velbrin Redesign of Website

I require my webpage to look different but this is out with my current providers platform
I will benefit from designs that use my wording (this is extremely important). I appreciate there may be a lot of wording in some areas so i would be happy with "read more" in various places. The use of my face in photo is a must and my logo is also a must which can be found on m y website www.velbrinadhd.co.uk I do not want corporate feel, i would like a warm, authentic. personal and inviting feel.

```html
<!DOCTYPE html>
<html lang="en">
<head>
<meta charset="utf-8">
<title>Velbrin – The Story Behind Velbrin</title>
<link href="https://fonts.googleapis.com/css2?family=Poppins:wght@400;500;600&display=swap" rel="stylesheet">
<style>
:root{
  --teal:#17a383;
  --teal-dark:#128a6f;
  --slate:#6f9a9f;
  --slate-soft:#dce9ea;
  --mint:#e9f5f2;
  --ink:#1c2325;
  --text:#3a4446;
  --line:#e2e7e8;
  --badge:#eef1f2;
  --footer:#24292b;
  --white:#fff;
}
*{box-sizing:border-box;margin:0;padding:0}
html,body{width:1200px;height:3883px;overflow:hidden}
body{font-family:'Poppins',sans-serif;color:var(--text);background:var(--white);position:relative}
.abs{position:absolute}
.topbar{left:0;top:0;width:1200px;height:63px;background:var(--slate)}
.topbar .call{left:914px;top:12px;display:flex;align-items:center;gap:12px;color:#fff}
.topbar .call small{display:block;font-size:12px;opacity:.9}
.topbar .call strong{font-size:15px;font-weight:600}
.ring{width:34px;height:34px;border-radius:50%;background:#fff;display:flex;align-items:center;justify-content:center}
.sidebar{left:0;top:63px;width:212px;height:3820px;background:#fff;border-right:1px solid var(--line)}
.brand{left:0;top:22px;width:212px;text-align:center}
.brand .mark{width:70px;height:70px;border-radius:50%;background:var(--slate);margin:0 auto 10px}
.brand span{font-size:18px;font-weight:600;color:var(--slate)}
.nav{top:175px;left:0;width:212px;list-style:none}
.nav li{display:flex;align-items:center;gap:12px;padding:0 16px;font-size:12.5px;font-weight:500;color:var(--ink);line-height:1.3;height:42px;margin-bottom:12px}
.nav li.active{background:var(--mint);border-right:3px solid var(--slate);height:46px}
.nav .ic{width:18px;height:18px;border:1.5px solid var(--slate);border-radius:50%;flex:none}
.hero{left:212px;top:63px;width:988px;height:563px;background:linear-gradient(120deg,#eef7f5 0%,#e2f1ee 55%,#d4e8e6 100%)}
.hero h1{left:41px;top:80px;width:440px;font-size:48px;line-height:57px;font-weight:600;color:var(--ink)}
.hero h1 em,.accent{color:var(--teal);font-style:normal}
.hero p{left:41px;top:258px;width:440px;font-size:14.5px;line-height:27.5px;color:var(--ink)}
.btn{display:flex;align-items:center;gap:8px;font-size:14px;border-radius:4px;padding:0 14px;height:44px}
.btn-solid{background:var(--teal);color:#fff}
.btn-ghost{border:1.5px solid #b9c9cb;color:#5b6b6e;background:#fff}
.hero .b1{left:41px;top:437px}
.hero .b2{left:254px;top:437px}
.hero .tab1{left:863px;top:43px;width:97px;height:52px;background:#8fdcc9;border-radius:6px}
.hero .portrait{left:498px;top:67px;width:415px;height:425px;border-radius:16px;border:3px solid #fff;background:linear-gradient(160deg,#d7dcdb,#bfc6c5 60%,#3a3a3a 100%)}
.hero .tab2{left:780px;top:492px;width:95px;height:27px;background:#fff;border-radius:0 0 6px 6px}
.sec-title{font-size:29px;font-weight:600;color:var(--ink);text-align:center}
.rule{width:62px;height:3px;background:var(--teal);margin:12px auto 0}
.why{left:253px;top:680px;width:904px}
.why .cols{display:flex;margin-top:28px}
.why .col{flex:1;text-align:center;border-right:1px solid var(--line);padding:0 18px;height:188px}
.why .col:last-child{border:none}
.why .icon{width:71px;height:71px;border-radius:50%;background:var(--slate-soft);margin:0 auto 22px;display:flex;align-items:center;justify-content:center}
.why .icon i{width:34px;height:34px;border-radius:50%;background:var(--slate);display:block}
.why p{font-size:14px;font-weight:500;line-height:25px;color:var(--ink)}
.hr{left:253px;top:1011px;width:904px;height:1px;background:var(--line)}
.photo{border-radius:14px;background:linear-gradient(135deg,#9aa3a6,#c7ccc9 50%,#5c6568)}
.lived-img{left:253px;top:1075px;width:318px;height:325px;border-top-right-radius:70px}
.lived{left:606px;top:1075px;width:550px}
.lived h2{font-size:27px;line-height:37px;font-weight:600;color:var(--ink);margin-bottom:8px}
.body{font-size:12.6px;line-height:24.5px;color:var(--text)}
.body+.body{margin-top:12px}
.landscape{left:253px;top:1457px;width:904px;height:368px;background:linear-gradient(180deg,#a9c6e4 0%,#b8c8d4 30%,#7b6b5c 45%,#3f5a46 60%,#5e7fa8 78%,#8a6d57 100%)}
.peri{left:253px;top:1853px;width:904px}
.peri h2{font-size:27px;font-weight:600;color:var(--ink)}
.peri .underline{width:62px;height:3px;background:var(--teal);margin:8px 0 18px}
.journey{left:253px;top:2235px;width:904px;height:409px;background:var(--teal);border-radius:8px}
.journey h2{color:#fff;font-size:29px;font-weight:600;text-align:center;margin-top:44px}
.journey .rule{background:#fff}
.cards{position:absolute;left:35px;top:112px;width:834px;display:grid;grid-template-columns:1fr 1fr;gap:20px 19px}
.card{background:#fff;border-radius:6px;height:104px;display:flex;align-items:center;gap:20px;padding:0 24px 0 16px}
.card:nth-child(n+3){height:120px}
.card .ci{width:70px;height:70px;border-radius:50%;background:var(--slate);flex:none}
.card p{font-size:12.6px;line-height:22.5px;color:var(--ink)}
.coach{left:253px;top:2700px;width:904px;text-align:center}
.coach h2{font-size:29px;font-weight:600;color:var(--ink)}
.coach h2 u{color:var(--teal);text-underline-offset:6px}
.coach p{width:820px;margin:22px auto 0;font-size:12.6px;line-height:24.5px}
.badges{left:389px;top:2889px;display:flex;gap:20px}
.badge{width:198px;height:143px;border:1.5px solid #d7dcdd;border-radius:4px;display:flex;align-items:center;justify-content:center}
.badge i{display:block;width:110px;height:80px;border-radius:6px;background:var(--badge)}
.privacy-btn{left:623px;top:3069px;width:165px;height:43px;background:var(--slate);color:#fff;border-radius:4px;justify-content:center}
.cta{left:253px;top:3177px;width:904px;height:246px;background:var(--slate);border-radius:14px;overflow:hidden}
.cta .ph{position:absolute;left:0;top:0;width:310px;height:246px;border-radius:0;clip-path:polygon(0 0,86% 0,100% 100%,0 100%)}
.cta h2{position:absolute;left:340px;top:38px;font-size:36px;line-height:48px;font-weight:500;color:#fff}
.cta h2 u{text-underline-offset:8px;text-decoration-thickness:2px}
.cta .btn{position:absolute;left:340px;top:151px;height:44px;background:#fff;color:#5b6b6e}
.footer{left:212px;top:3488px;width:988px;height:395px;background:var(--footer);color:#d5dbdc}
.footer .flogo{left:36px;top:60px;width:240px;text-align:center}
.footer .flogo .mark{width:84px;height:84px;border-radius:50%;background:var(--slate);margin:0 auto 14px}
.footer .flogo span{font-size:18px;font-weight:600;color:var(--slate)}
.footer h4{font-size:15px;font-weight:600;color:#fff;margin-bottom:22px}
.footer .links{left:387px;top:47px}
.footer .links a{display:block;font-size:12.8px;color:#d5dbdc;text-decoration:none;line-height:29px}
.footer .contact{left:724px;top:47px;width:240px}
.footer .row{display:flex;gap:14px;font-size:12.8px;line-height:22px;margin-bottom:18px;align-items:center}
.footer .row .ring{width:30px;height:30px;background:#3a4244;flex:none}
.footer .row .ring.on{background:var(--teal)}
.footer .bar{left:40px;top:305px;width:908px;height:1px;background:#3a4244}
.footer .copy{left:40px;top:338px;font-size:12.8px}
.social{left:800px;top:330px;display:flex;gap:12px}
.social span{width:28px;height:28px;border-radius:50%;border:1.5px solid #9aa5a7}
.social span:first-child{background:var(--teal);border-color:var(--teal)}
</style>
</head>
<body>

<header class="abs topbar">
  <div class="abs call">
    <span class="ring"><svg width="16" height="16" viewBox="0 0 24 24"><path d="M6.6 10.8a15.1 15.1 0 0 0 6.6 6.6l2.2-2.2a1 1 0 0 1 1-.25 11.4 11.4 0 0 0 3.6.57 1 1 0 0 1 1 1V20a1 1 0 0 1-1 1A17 17 0 0 1 3 4a1 1 0 0 1 1-1h3.5a1 1 0 0 1 1 1c0 1.250.2 2.45.57 3.57a1 1 0 0 1-.25 1z" fill="#6f9a9f"/></svg></span>
    <div><small>Call Us:</small><strong>0131 555 0192</strong></div>
  </div>
</header>

<aside class="abs sidebar">
  <div class="abs brand"><div class="mark"></div><span>Velbrin</span></div>
  <ul class="abs nav">
    <li class="active"><span class="ic"></span>The Story Behind Velbrin</li>
    <li><span class="ic"></span>How Velbrin Can Support You</li>
    <li><span class="ic"></span>Organisation &amp; School Partnerships</li>
    <li style="height:28px"><span class="ic"></span>Resources</li>
    <li style="height:28px"><span class="ic"></span>Contact Velbrin</li>
    <li style="height:28px"><span class="ic"></span>Privacy Policy</li>
  </ul>
</aside>

<section class="abs hero">
  <h1 class="abs">Helping People with ADHD <em>Unlock Their Potential</em></h1>
  <p class="abs">My adult ADHD diagnosis came during a period of profound self-discovery following a mental health breakdown. While studying Integrative Counselling at the University of the Northern Isles, I began to understand myself in ways I never had before.</p>
  <a class="abs btn btn-solid b1"><svg width="18" height="18" viewBox="0 0 24 24" fill="none" stroke="#fff" stroke-width="2"><rect x="3" y="5" width="18" height="16" rx="2"/><path d="M3 10h18M8 3v4M16 3v4"/></svg>Book a Consultation</a>
  <a class="abs btn btn-ghost b2"><svg width="20" height="20" viewBox="0 0 24 24" fill="none" stroke="#5b6b6e" stroke-width="1.8"><circle cx="12" cy="12" r="9"/><path d="M12 11v6M12 7.5v.5"/></svg>Learn More</a>
  <div class="abs tab1"></div>
  <div class="abs portrait photo" role="img" aria-label="Portrait photo of the Velbrin founder"></div>
  <div class="abs tab2"></div>
</section>

<section class="abs why">
  <h2 class="sec-title">Why Velbrin Was Created</h2>
  <div class="rule"></div>
  <div class="cols">
    <div class="col"><div class="icon"><i></i></div><p>I wanted to offer the kind of support I wish I had when I was struggling.</p></div>
    <div class="col"><div class="icon"><i></i></div><p>I believe in practical, lasting support.</p></div>
    <div class="col"><div class="icon"><i></i></div><p>I understand the reality of neurodivergent family life.</p></div>
    <div class="col"><div class="icon"><svg width="36" height="40" viewBox="0 0 24 26"><path d="M12 1l10 4v7c0 6.5-4.3 11.4-10 13C6.3 23.4 2 18.5 2 12V5z" fill="#6f9a9f"/><path d="M7.5 13l3 3 6-6" stroke="#fff" stroke-width="2" fill="none"/></svg></div><p>My personal experiences and professional qualifications shape the compassionate,</p></div>
  </div>
</section>
<div class="abs hr"></div>

<div class="abs lived-img photo" role="img" aria-label="Photo of the founder bottle-feeding a lamb on a farm"></div>
<section class="abs lived">
  <h2>Velbrin was created from both lived experience and <span class="accent">professional expertise.</span></h2>
  <p class="body">My adult ADHD diagnosis came during a period of profound self-discovery following a mental health breakdown. While studying Integrative Counselling at the University of the Northern Isles, I began to understand myself in ways I never had before.</p>
  <p class="body">For many years, my ADHD had gone unrecognised, and I was treated only with antidepressants, which never addressed the underlying cause of my struggles. Learning about ADHD didn't cause my breakdown—it helped explain it. It gave me the answers I had been searching for and marked the beginning of a journey towards greater self-understanding and self-compassion.</p>
</section>

<div class="abs landscape photo" role="img" aria-label="Landscape photo of a loch surrounded by pine forest and moorland hills"></div>

<section class="abs peri">
  <h2>As a woman navigating both ADHD and <span class="accent">perimenopause</span>,</h2>
  <div class="underline"></div>
  <p class="body">I have also experienced first-hand how hormonal changes can make neurodivergent traits more noticeable and difficult to manage. Declining oestrogen levels can affect dopamine, a neurotransmitter closely linked to attention, motivation, memory and emotional regulation. For many women, perimenopause is the stage of life where ADHD traits become more apparent, or previously successful coping strategies suddenly stop working.</p>
  <p class="body">Understanding these connections strengthened my passion for helping neurodivergent individuals better understand their brains, develop self-compassion and discover practical strategies that genuinely support their wellbeing.</p>
  <p class="body">This personal journey inspired me to deepen my professional knowledge. I completed a Higher National Qualification in Integrative Counselling, gaining valuable self-awareness alongside practical and theoretical skills. While I chose not to continue into the final year, I realised my passion lay in offering a more holistic approach—one that went beyond simply providing a listening ear. I wanted to empower people with practical knowledge, strategies and tools that they could continue using long after our work together had ended.</p>
</section>

<section class="abs journey">
  <h2>My Journey</h2>
  <div class="rule"></div>
  <div class="cards">
    <div class="card"><span class="ci"></span><p>My adult ADHD diagnosis came during a period of profound self-discovery following a mental health breakdown.</p></div>
    <div class="card"><span class="ci"></span><p>As my understanding grew, I recognised I am also autistic something that is common alongside ADHD.</p></div>
    <div class="card"><span class="ci"></span><p>These experiences strengthened my passion for helping neurodivergent individuals better understand their brains, develop self-compassion and find strategies that work.</p></div>
    <div class="card"><span class="ci"></span><p>This personal journey inspired me to deepen my professional knowledge and training.</p></div>
  </div>
</section>

<section class="abs coach">
  <h2>Coaching <u>Qualifications</u></h2>
  <p>I have also experienced first-hand how hormonal changes can make neurodivergent traits more noticeable and difficult to manage. Declining oestrogen levels can affect dopamine, a neurotransmitter closely linked to attention, motivation, memory and emotional regulation. For many women, perimenopause is the stage of life where ADHD traits become more apparent, or previously successful coping strategies suddenly stop working.</p>
</section>
<div class="abs badges">
  <div class="badge" role="img" aria-label="Coaching qualification badge"><i></i></div>
  <div class="badge" role="img" aria-label="Accredited coach training badge"><i></i></div>
  <div class="badge" role="img" aria-label="Care institute accreditation badge"><i></i></div>
</div>
<a class="abs btn privacy-btn"><svg width="16" height="18" viewBox="0 0 24 26"><path d="M12 1l10 4v7c0 6.5-4.3 11.4-10 13C6.3 23.4 2 18.5 2 12V5z" fill="#fff"/><path d="M7.5 13l3 3 6-6" stroke="#6f9a9f" stroke-width="2.4" fill="none"/></svg>Privacy Policy</a>

<section class="abs cta">
  <div class="ph photo" role="img" aria-label="Photo of the founder feeding lambs"></div>
  <h2>Discover your inner strength<br>and cultivate a <u>balanced life</u></h2>
  <a class="btn"><svg width="18" height="18" viewBox="0 0 24 24" fill="none" stroke="#5b6b6e" stroke-width="2"><rect x="3" y="5" width="18" height="16" rx="2"/><path d="M3 10h18M8 3v4M16 3v4"/></svg>Book a Consultation</a>
</section>

<footer class="abs footer">
  <div class="abs flogo"><div class="mark"></div><span>Velbrin</span></div>
  <div class="abs links">
    <h4>Solutions</h4>
    <a>The Story Behind Velbrin</a><a>How Velbrin Can Support You</a><a>Organisation &amp; School Partnerships</a><a>Resources</a><a>Contact Velbrin</a><a>Privacy Policy</a>
  </div>
  <div class="abs contact">
    <h4>Solutions</h4>
    <div class="row"><span class="ring"><svg width="14" height="16" viewBox="0 0 24 28"><path d="M12 1a9 9 0 0 0-9 9c0 7 9 17 9 17s9-10 9-17a9 9 0 0 0-9-9z" fill="none" stroke="#d5dbdc" stroke-width="2.4"/><circle cx="12" cy="10" r="3" fill="#d5dbdc"/></svg></span>123, Lorem ipsum dolor sit amet, consectetur - 52100</div>
    <div class="row"><span class="ring on"><svg width="14" height="14" viewBox="0 0 24 24"><path d="M6.6 10.8a15.1 15.1 0 0 0 6.6 6.6l2.2-2.2a1 1 0 0 1 1-.25 11.4 11.4 0 0 0 3.6.57 1 1 0 0 1 1 1V20a1 1 0 0 1-1 1A17 17 0 0 1 3 4a1 1 0 0 1 1-1h3.5a1 1 0 0 1 1 1c0 1.25.2 2.45.57 3.57a1 1 0 0 1-.25 1z" fill="#fff"/></svg></span>Phone: (0131)-555 0192</div>
    <div class="row"><span class="ring"><svg width="14" height="12" viewBox="0 0 24 18"><rect x="1" y="1" width="22" height="16" rx="2" fill="none" stroke="#d5dbdc" stroke-width="2"/><path d="M1 2l11 8 11-8" fill="none" stroke="#d5dbdc" stroke-width="2"/></svg></span>info@velbrinadhd.com</div>
  </div>
  <div class="abs bar"></div>
  <div class="abs copy">© 2026. All Rights Reserved.</div>
  <div class="abs social"><span></span><span></span><span></span><span></span></div>
</footer>

</body>
</html>
```